Landing Page Design für Immobilienbüro
Zielgruppe
Wir sind ein regionales Immobilienbüro, spezialisiert auf den Verkauf bzw. die Vermittlung von Immobilien, vorwiegend im Bereich der Wohnimmobilien.
Wir wollen unseren Bekanntheitsgrad zunächst in der Region und zukünftig auch regionsübergreifend erweitern, stärken und dauerhaft Marktanteile sichern.
Hierzu möchten wir zielgruppenorientierte Landingpages einsetzen, welche auch via Plaxo-Ads etc. beworben werden und suchmaschinenfreundlich gestaltet sind soll. Hier ist also neben der kreativen Fachkenntnis auch Kenntnis in SEO etc. gefragt.
Auch könnten wir uns eine dauerhafte, auch auf Erfolg basierte Zusammenarbeit vorstellen.
Zielgruppen für die Landingpage:
Personen, welche eine Immobilie geerbt haben
Personen, deren Immobilie zu groß / zu klein ist
Personen, die sich trennen und die Immobilie deswegen verkauft werden muss
Aufgabenstellung
Die Landingpage soll jeweils an unser CI (siehe haus-lotsen.immo) angepasst sein, so dass der Wiedererkennungswert steigt. Die Seite soll die Möglichkeit eines Kontaktformulars, eines Videos, Einbindung von Kundenmeinungen etc. beinhalten.

```html
<!DOCTYPE html>
<html lang="de">
<head>
<meta charset="utf-8">
<title>haus-lotsen.immo – Landingpage</title>
<link rel="stylesheet" href="https://fonts.googleapis.com/css2?family=Rubik:wght@500;700&family=Raleway:wght@300;400;500;600&display=swap">
<style>
:root{
  --blue:#3b64a3;
  --green:#76b82a;
  --mint:#effcfc;
  --text:#555c66;
  --muted:#8b929a;
  --white:#ffffff;
  --line:#e6e9ec;
}
*{box-sizing:border-box;margin:0;padding:0}
html,body{width:1200px;height:3207px;overflow:hidden;background:var(--white)}
body{position:relative;font-family:'Raleway',sans-serif;color:var(--text)}
.abs{position:absolute}
.backdrop{left:0;top:0}
.brand{left:93px;top:34px;display:flex;align-items:center;gap:14px;color:var(--white);font-family:'Rubik',sans-serif;font-weight:500;font-size:40px;letter-spacing:-.5px}
.brand-mark{width:34px;height:34px;border-radius:50%;background:var(--white)}
.contact{top:52px;display:flex;align-items:center;gap:8px;color:var(--white);font-family:'Rubik',sans-serif;font-weight:500;font-size:16px}
.contact.phone{left:712px}
.contact.mail{left:888px}
.social{top:219px;width:34px;height:34px;border-radius:50%;background:var(--white);opacity:.9}
.booking-title{left:743px;width:330px;top:312px;text-align:center;font-family:'Rubik',sans-serif;font-weight:700;font-size:28px;color:var(--blue)}
.field{left:743px;width:331px;height:46px;border:1.5px solid var(--green);background:var(--white);font-size:13px;color:var(--muted);padding:14px 10px}
.field.message{height:88px}
.btn{display:flex;align-items:center;justify-content:center;font-family:'Raleway',sans-serif;font-weight:500}
.btn-green{background:var(--green);color:var(--white)}
.callback{left:743px;top:673px;width:202px;height:54px;font-size:17px}
.offer-kicker{left:0;width:1200px;top:836px;text-align:center;font-weight:300;font-size:42px;color:var(--green)}
.offer-title{left:0;width:1208px;top:884px;text-align:center;font-family:'Rubik',sans-serif;font-weight:700;font-size:42px;color:var(--blue)}
.listing{top:979px;width:326px;height:254px;background:var(--white);border:1px solid #dfe3e6}
.listing-photo{position:absolute;left:0;top:0;width:100%;height:204px;background:linear-gradient(180deg,#8fb3d6 0%,#b7c9b8 45%,#5b8f3a 70%,#6aad2e 100%)}
.listing-badge{position:absolute;left:12px;top:12px;background:var(--green);color:var(--white);font-family:'Rubik',sans-serif;font-weight:500;font-size:16px;padding:6px 10px}
.listing-icons{position:absolute;right:16px;top:168px;display:flex;gap:14px}
.listing-price{position:absolute;left:8px;top:219px;background:var(--blue);color:var(--white);font-family:'Rubik',sans-serif;font-weight:500;font-size:15px;padding:6px 8px}
.listing-size{position:absolute;right:17px;top:222px;color:var(--blue);font-family:'Rubik',sans-serif;font-weight:500;font-size:17px}
.dot{width:8px;height:8px;border-radius:50%;background:var(--blue)}
.dot.active{width:14px;height:14px;background:var(--green)}
.divider{left:110px;width:980px;height:3px;background:linear-gradient(90deg,transparent,var(--line) 20%,var(--line) 80%,transparent)}
.video-title{left:92px;top:1470px;width:360px;font-family:'Rubik',sans-serif;font-weight:700;font-size:42px;line-height:52px;color:var(--blue)}
.video-copy{left:92px;top:1580px;width:350px;font-size:19px;line-height:37.7px;color:var(--text)}
.more{left:92px;top:1850px;width:150px;height:40px;font-family:'Rubik',sans-serif;font-size:18px}
.video{left:464px;top:1467px;width:643px;height:427px;background:linear-gradient(135deg,#e9ecef 0%,#cfd6dc 45%,#9aa7b3 100%)}
.play{position:absolute;left:295px;top:173px;width:76px;height:76px;border-radius:50%;background:var(--white);display:flex;align-items:center;justify-content:center}
.reviews-title{left:0;width:1190px;top:2102px;text-align:center;font-family:'Rubik',sans-serif;font-weight:700;font-size:42px;color:var(--blue)}
.avatar{top:2215px;width:214px;height:214px;border-radius:50%;border:6px solid var(--white);box-shadow:0 4px 14px rgba(0,0,0,.12)}
.review-name{top:2463px;width:284px;text-align:center;font-weight:500;font-size:26px;color:var(--green)}
.review-text{top:2508px;width:284px;font-weight:300;font-size:17.5px;line-height:30.5px;color:var(--muted);text-align:justify;text-align-last:center}
.sell-kicker{left:92px;top:2866px;font-size:22px;color:var(--green)}
.sell-title{left:92px;top:2898px;font-family:'Rubik',sans-serif;font-weight:700;font-size:44px;color:var(--green)}
.sell-copy{left:92px;top:2973px;width:632px;font-size:18px;line-height:30.5px;color:var(--white);text-align:justify}
.submit{left:829px;top:2932px;width:190px;height:54px;font-size:20px}
.buy{left:829px;top:3002px;width:190px;height:54px;font-size:20px;background:var(--white);color:var(--blue)}
.footer{left:0;width:1200px;top:3162px;text-align:center;color:var(--white);font-size:19px}
</style>
</head>
<body>

<svg class="abs backdrop" width="1200" height="3207" viewBox="0 0 1200 3207">
  <defs>
    <linearGradient id="heroPhoto" x1="0" y1="0" x2="1" y2="1">
      <stop offset="0" stop-color="#7fa683"/>
      <stop offset=".5" stop-color="#9db59c"/>
      <stop offset="1" stop-color="#6f8f78"/>
    </linearGradient>
  </defs>
  <rect x="0" y="240" width="1200" height="552" fill="var(--mint)"/>
  <path d="M680,790 C600,1000 320,1150 80,1402 C72,1300 150,1180 260,1080 C400,950 470,860 430,790 Z" fill="var(--mint)"/>
  <path role="img" aria-label="Foto einer lachenden Familie im Wohnzimmer unter einem Hausdach-Symbol" d="M0,0 H1200 V282 C1120,300 1060,270 1000,250 C900,222 780,232 730,300 C690,360 702,460 690,560 C680,660 620,700 520,722 C400,744 300,705 200,735 C120,758 60,780 0,742 Z" fill="url(#heroPhoto)"/>
  <path d="M0,2851 C140,2790 200,2760 300,2760 C420,2760 470,2840 620,2840 C800,2840 1000,2720 1200,2695 V3207 H0 Z" fill="var(--blue)"/>
</svg>

<header>
  <div class="abs brand"><span class="brand-mark"></span>haus-lotsen.immo</div>
  <div class="abs contact phone">
    <svg width="14" height="20" viewBox="0 0 14 20"><path d="M3 1 L6 1 L7 6 L5 8 C6 11 8 13 10 14 L12 12 L14 14 L14 17 C14 19 12 19 10 18 C5 16 1 11 1 5 C1 3 1 1 3 1 Z" fill="#fff"/></svg>
    +19 4820 366 17
  </div>
  <div class="abs contact mail">
    <svg width="24" height="16" viewBox="0 0 24 16"><rect x="1" y="1" width="22" height="14" fill="none" stroke="#fff" stroke-width="2"/><path d="M1 1 L12 9 L23 1" fill="none" stroke="#fff" stroke-width="2"/></svg>
    info@haus-lotsen.immo
  </div>
  <span class="abs social" style="left:949px" aria-label="Soziales Netzwerk"></span>
  <span class="abs social" style="left:1001px" aria-label="Soziales Netzwerk"></span>
  <span class="abs social" style="left:1052px" aria-label="Soziales Netzwerk"></span>
</header>

<section class="booking">
  <h2 class="abs booking-title">Termin Buchen</h2>
  <div class="abs field" style="top:381px">Name*</div>
  <div class="abs field" style="top:441px">E-Mail Adresse*</div>
  <div class="abs field" style="top:500px">Ruckrufnummer*</div>
  <div class="abs field message" style="top:561px">Nachricht</div>
  <div class="abs btn btn-green callback">Rückruf anfordern</div>
</section>

<section class="offers">
  <p class="abs offer-kicker">Wir bieten die besten Immobilien</p>
  <h2 class="abs offer-title">Bestes Haus für Sie</h2>

  <article class="abs listing" style="left:92px">
    <div class="listing-photo" role="img" aria-label="Foto eines Hauses mit Rasen"></div>
    <span class="listing-badge">Obstgarten</span>
    <div class="listing-icons">
      <svg width="28" height="24" viewBox="0 0 28 24"><path d="M14 22 C4 14 1 10 1 6.5 C1 3 4 1 7 1 C10 1 12 3 14 5 C16 3 18 1 21 1 C24 1 27 3 27 6.5 C27 10 24 14 14 22 Z" fill="none" stroke="#fff" stroke-width="2"/></svg>
      <svg width="26" height="26" viewBox="0 0 26 26"><circle cx="20" cy="5" r="3.5" fill="none" stroke="#fff" stroke-width="2"/><circle cx="6" cy="13" r="3.5" fill="none" stroke="#fff" stroke-width="2"/><circle cx="20" cy="21" r="3.5" fill="none" stroke="#fff" stroke-width="2"/><path d="M9 11 L17 7 M9 15 L17 19" stroke="#fff" stroke-width="2"/></svg>
    </div>
    <span class="listing-price">$ 80,650.00</span>
    <span class="listing-size">1026 sq ft</span>
  </article>

  <article class="abs listing" style="left:438px">
    <div class="listing-photo" role="img" aria-label="Foto eines Steinhauses mit Rasen"></div>
    <span class="listing-badge">Obstgarten</span>
    <div class="listing-icons">
      <svg width="28" height="24" viewBox="0 0 28 24"><path d="M14 22 C4 14 1 10 1 6.5 C1 3 4 1 7 1 C10 1 12 3 14 5 C16 3 18 1 21 1 C24 1 27 3 27 6.5 C27 10 24 14 14 22 Z" fill="none" stroke="#fff" stroke-width="2"/></svg>
      <svg width="26" height="26" viewBox="0 0 26 26"><circle cx="20" cy="5" r="3.5" fill="none" stroke="#fff" stroke-width="2"/><circle cx="6" cy="13" r="3.5" fill="none" stroke="#fff" stroke-width="2"/><circle cx="20" cy="21" r="3.5" fill="none" stroke="#fff" stroke-width="2"/><path d="M9 11 L17 7 M9 15 L17 19" stroke="#fff" stroke-width="2"/></svg>
    </div>
    <span class="listing-price">$ 80,650.00</span>
    <span class="listing-size">1026 sq ft</span>
  </article>

  <article class="abs listing" style="left:782px">
    <div class="listing-photo" role="img" aria-label="Foto eines Landhauses mit Garten"></div>
    <span class="listing-badge">Obstgarten</span>
    <div class="listing-icons">
      <svg width="28" height="24" viewBox="0 0 28 24"><path d="M14 22 C4 14 1 10 1 6.5 C1 3 4 1 7 1 C10 1 12 3 14 5 C16 3 18 1 21 1 C24 1 27 3 27 6.5 C27 10 24 14 14 22 Z" fill="none" stroke="#fff" stroke-width="2"/></svg>
      <svg width="26" height="26" viewBox="0 0 26 26"><circle cx="20" cy="5" r="3.5" fill="none" stroke="#fff" stroke-width="2"/><circle cx="6" cy="13" r="3.5" fill="none" stroke="#fff" stroke-width="2"/><circle cx="20" cy="21" r="3.5" fill="none" stroke="#fff" stroke-width="2"/><path d="M9 11 L17 7 M9 15 L17 19" stroke="#fff" stroke-width="2"/></svg>
    </div>
    <span class="listing-price">$ 80,650.00</span>
    <span class="listing-size">1026 sq ft</span>
  </article>

  <span class="abs dot active" style="left:584px;top:1286px"></span>
  <span class="abs dot" style="left:611px;top:1289px"></span>
  <span class="abs dot" style="left:631px;top:1289px"></span>
</section>

<div class="abs divider" style="top:1369px"></div>

<section class="video-block">
  <h2 class="abs video-title">Das Mordan Haus Video</h2>
  <p class="abs video-copy">Eines der weltweit führenden Immobilienunternehmen und Deutschlands größter unabhängiger Immobilienmakler. In Deutschland sind wir seit 1977 in der Vermittlung hochwertiger Wohnimmobilien tätig.</p>
  <div class="abs btn btn-green more">Mehr wissen</div>
  <div class="abs video" role="img" aria-label="Videovorschau: Paar mit Maklerin in einer hellen Küche">
    <span class="play"><svg width="26" height="30" viewBox="0 0 26 30"><path d="M2 1 L25 15 L2 29 Z" fill="var(--green)"/></svg></span>
  </div>
</section>

<div class="abs divider" style="top:2041px"></div>

<section class="reviews">
  <h2 class="abs reviews-title">Was Kunden sagen</h2>

  <div class="abs avatar" style="left:136px;background:linear-gradient(160deg,#f2f2f2,#d9c2b0)" role="img" aria-label="Porträtfoto einer Kundin"></div>
  <h3 class="abs review-name" style="left:96px">Selma Varin Okuda</h3>
  <p class="abs review-text" style="left:92px">Lorem ipsum dolor consectetur iicing elit, sed do eius Lorem ipsum dolo amet, costur adipisicing eiusmod. Lorem ipsum dolor consectetur iicing elit, sed do eius.</p>

  <div class="abs avatar" style="left:493px;background:linear-gradient(160deg,#f4f4f4,#cfd8e4)" role="img" aria-label="Porträtfoto eines Kunden"></div>
  <h3 class="abs review-name" style="left:461px">Jonas Terbeck</h3>
  <p class="abs review-text" style="left:460px">Lorem ipsum dolor consectetur iicing elit, sed do eius Lorem ipsum dolo amet, costur adipisicing eiusmod. Lorem ipsum dolor consectetur iicing elit, sed do eius.</p>

  <div class="abs avatar" style="left:847px;background:linear-gradient(160deg,#e9eee0,#b89a78)" role="img" aria-label="Porträtfoto einer Kundin"></div>
  <h3 class="abs review-name" style="left:820px">Oriana Bellweg</h3>
  <p class="abs review-text" style="left:824px">Lorem ipsum dolor consectetur iicing elit, sed do eius Lorem ipsum dolo amet, costur adipisicing eiusmod. Lorem ipsum dolor consectetur iicing elit, sed do eius.</p>

  <span class="abs dot active" style="left:584px;top:2711px"></span>
  <span class="abs dot" style="left:611px;top:2714px"></span>
  <span class="abs dot" style="left:631px;top:2714px"></span>
</section>

<section class="sell">
  <p class="abs sell-kicker">Kaufen oder verkaufen</p>
  <h2 class="abs sell-title">Objekt einreichen</h2>
  <p class="abs sell-copy">consecte Lorem ipsum dolor sit amet, Lorem ipsum dolor amet, consecte Lorem ipsum dolor sit adipisicing amet, consectetur sed do eiusmod tempor incididunt dolore magna consecrem adipisicing ipsum dolor sit amet, consectetur elit,</p>
  <div class="abs btn btn-green submit">Einreichen</div>
  <div class="abs btn buy">Kaufe Jetzt</div>
</section>

<footer class="abs footer">© 2021 Haus-Lotsen. Mit &nbsp;Liebe gemacht.</footer>

</body>
</html>
```